Duel Business card

Want an edgy business card that shows both of our companies on each side of the card, OR both together with a cool design.

*Must be edgy: We have attached our two business logos. We are a bail bond and immigration bond company.

Would like the address on one side only.
Need Phone, cell, website, address, and Name

Company Name 1: Cellgate Release Partners
www.cellgatereleasepartners.example

Company Name 2: Borderline Surety Associates
www.borderlinesuretyassociates.example

These cards will need to be easily changeable so I can modify new employees

Target Market(s)

people in jail, takign imigrants out of jail and from being taken back to there country

Industry/Entity Type

Business

Requirements
Must have
• Include both logos attached

```html
<!DOCTYPE html>
<html lang="en">
<head>
<meta charset="utf-8">
<title>Dual Business Card – Cellgate Release Partners &amp; Borderline Surety Associates</title>
<link rel="stylesheet" href="https://fonts.googleapis.com/css2?family=Rubik:wght@400;500;600;700&display=swap">
<style>
  :root {
    --navy: #1b318c;
    --gold: #e8b92f;
    --red: #ee1c2a;
    --white: #ffffff;
    --ink: #1d1d1f;
    --label: #1b318c;
    --stage-light: #f7f7f7;
    --stage-dark: #bdbdbd;
  }
  * { margin: 0; padding: 0; box-sizing: border-box; }
  html, body { width: 1200px; height: 900px; overflow: hidden; }
  body {
    font-family: "Rubik", Arial, sans-serif;
    background: radial-gradient(ellipse at 50% 50%, var(--stage-light) 0%, #e2e2e2 55%, var(--stage-dark) 100%);
    position: relative;
  }
  .card {
    position: absolute;
    width: 509px;
    height: 311px;
    border-radius: 20px;
    overflow: hidden;
    box-shadow: 3px 5px 8px rgba(0,0,0,0.35);
  }
  .card--front { background: var(--white); left: 63px; }
  .card--back { background: var(--navy); left: 624px; }
  .row-top { top: 113px; }
  .row-bottom { top: 470px; }

  /* front side */
  .brand-band {
    position: absolute; left: 45px; top: 0; width: 168px; height: 100%;
    background: var(--navy);
    display: flex; flex-direction: column; align-items: center;
  }
  .brand {
    display: flex; flex-direction: column; align-items: center;
    color: var(--white); font-weight: 700; text-align: center;
    text-transform: uppercase; line-height: 1.1;
  }
  .brand__dot { width: 40px; height: 40px; border-radius: 50%; margin-bottom: 6px; }
  .brand--release { margin-top: 30px; font-size: 15px; }
  .brand--release .brand__dot { background: var(--gold); }
  .brand--surety { margin-top: 50px; font-size: 12px; }
  .brand--surety .brand__dot { background: var(--white); width: 46px; height: 46px; }

  .holder { position: absolute; left: 275px; top: 48px; }
  .holder__name { font-size: 16px; font-weight: 500; color: var(--ink); }
  .holder__role { font-size: 11px; color: var(--ink); margin-top: 3px; }

  .contact { position: absolute; left: 255px; top: 172px; list-style: none; }
  .contact li { display: flex; align-items: center; height: 21.6px; font-size: 11px; color: var(--ink); }
  .contact b { width: 15px; color: var(--label); font-weight: 700; font-size: 11px; }

  .accent-bar { position: absolute; right: 0; top: 170px; width: 10px; height: 100px; background: var(--red); }

  /* back side */
  .back-brand {
    position: absolute; left: 0; right: 0; top: 34px;
    display: flex; flex-direction: column; align-items: center;
    color: var(--white); font-weight: 700; text-transform: uppercase; text-align: center;
  }
  .back-brand__dot { border-radius: 50%; margin-bottom: 12px; }
  .back-brand--surety .back-brand__dot { width: 140px; height: 140px; background: var(--white); border: 3px solid #d9d9d9; }
  .back-brand--surety { font-size: 17px; top: 26px; }
  .back-brand--release .back-brand__dot { width: 72px; height: 72px; background: var(--gold); margin-top: 24px; }
  .back-brand--release { font-size: 28px; line-height: 1; }
  .back-url {
    position: absolute; left: 0; right: 0; top: 250px; text-align: center;
    color: var(--white); font-size: 18px; letter-spacing: 0.2px;
  }
  .back-url--release { top: 248px; font-weight: 500; }
</style>
</head>
<body>

  <!-- Front, row 1 -->
  <section class="card card--front row-top">
    <div class="brand-band">
      <div class="brand brand--release"><span class="brand__dot"></span>Cellgate Release<br>Partners</div>
      <div class="brand brand--surety"><span class="brand__dot"></span>Borderline Surety<br>Associates</div>
    </div>
    <div class="holder">
      <p class="holder__name">Daniel Verhoek</p>
      <p class="holder__role">Manager</p>
    </div>
    <ul class="contact">
      <li><b>P</b>1-800-555-0147</li>
      <li><b>P</b>1-800-555-0192</li>
      <li><b>M</b>dverhoek@cellgatereleasepartners.example</li>
      <li><b>W</b>www.cellgatereleasepartners.example</li>
      <li><b>W</b>www.borderlinesuretyassociates.example</li>
    </ul>
    <span class="accent-bar"></span>
  </section>

  <!-- Back, row 1 -->
  <section class="card card--back row-top">
    <div class="back-brand back-brand--surety"><span class="back-brand__dot"></span>Borderline Surety Associates</div>
    <p class="back-url">www.borderlinesuretyassociates.example</p>
  </section>

  <!-- Front, row 2 -->
  <section class="card card--front row-bottom">
    <div class="brand-band">
      <div class="brand brand--release"><span class="brand__dot"></span>Cellgate Release<br>Partners</div>
      <div class="brand brand--surety"><span class="brand__dot"></span>Borderline Surety<br>Associates</div>
    </div>
    <div class="holder">
      <p class="holder__name">Daniel Verhoek</p>
      <p class="holder__role">Manager</p>
    </div>
    <ul class="contact">
      <li><b>P</b>1-800-555-0147</li>
      <li><b>P</b>1-800-555-0192</li>
      <li><b>M</b>dverhoek@cellgatereleasepartners.example</li>
      <li><b>W</b>www.cellgatereleasepartners.example</li>
      <li><b>W</b>www.borderlinesuretyassociates.example</li>
    </ul>
    <span class="accent-bar"></span>
  </section>

  <!-- Back, row 2 -->
  <section class="card card--back row-bottom">
    <div class="back-brand back-brand--release"><span class="back-brand__dot"></span>Cellgate Release<br>Partners</div>
    <p class="back-url back-url--release">www.cellgatereleasepartners.example</p>
  </section>

</body>
</html>
```